Hollowmere Farm Promotional Leaflet

The team at Hollowmere Farm can help with every aspect of managing and enhancing your home from housekeeping and professional cleaning, laundry and ironing to providing chic and contemporary flower arrangements and even food for your pets!We take pride in providing high-end, consistent and reliable professional services bespoke to you. Whether you are a busy professional working long hours, a stay-at home parent or retired; having professional help in the home gives you time to spend on the things you enjoy.We are providing a very upmarket, highly professional service and need an A5 promotional leaflet to be designed. Please refer to www.hollowmerefarm-example.co.uk and see the section on 'Home Management'The leaflet should incorporate the Hollowmere Farm logo without the 'tipi', and any suitable photography images used on the home page of the website or the 'home management' section.

Target Market(s)

high-end, affluent owners of luxury homes

Industry/Entity Type

Farm

Contact Information for Business Card

The business card design needs to be suitable for use across all of Hollowmere Farm businesses, specifically:
Hollowmere Farm Home Management - otherwise known as Hollowmere Farm @ Home (this uses the typographical logo
Hollowmere Farm Weddings & Events - this uses the 'tipi' logo

Requirements
Must have
• Design in keeping with the look and feel of the logo and website design
• www.hollowmerefarm-example.co.uk

```html
<!DOCTYPE html>
<html lang="en">
<head>
<meta charset="utf-8">
<title>Hollowmere Farm Home Management – Leaflet</title>
<link href="https://fonts.googleapis.com/css2?family=Cinzel:wght@400;700&family=Lato:wght@400;700&display=swap" rel="stylesheet">
<style>
:root{
  --pink:#e0338f;
  --pink-deep:#c91f7c;
  --pink-soft:#f27ab8;
  --gold:#c99a3c;
  --gold-light:#e2bc62;
  --ink:#3a3a3a;
  --stage:#e6e6e6;
  --paper:#ffffff;
}
*{margin:0;padding:0;box-sizing:border-box}
html,body{width:1200px;height:1200px;overflow:hidden;background:var(--stage)}
.leaflet{position:absolute;left:200px;top:35px;width:800px;height:1130px;background:var(--paper);overflow:hidden;font-family:'Lato',sans-serif;color:var(--ink);box-shadow:0 6px 24px rgba(0,0,0,.15)}
.leaflet-shapes{position:absolute;inset:0}
.tagline{position:absolute;left:40px;top:34px;width:300px;font-family:'Cinzel',serif;font-size:19px;line-height:1.22;color:#fff;font-variant:small-caps;letter-spacing:.5px}
.logo-disc{position:absolute;left:62px;top:312px;width:216px;height:216px;border-radius:50%;display:flex;align-items:center;justify-content:center;text-align:center}
.logo-name{font-family:'Cinzel',serif;font-weight:400;font-size:26px;line-height:1.15;color:var(--pink)}
.title{position:absolute;left:40px;top:552px;font-family:'Cinzel',serif;line-height:1}
.title-main{display:block;font-size:40px;font-weight:700;color:var(--pink)}
.title-sub{display:block;font-size:35px;color:var(--gold);margin-top:6px}
.intro-pill{position:absolute;left:30px;top:655px;width:415px;padding:13px 22px;border:3px solid var(--gold);border-radius:30px;background:linear-gradient(90deg,var(--pink-soft),var(--pink-deep));color:#fff;font-size:17px;line-height:1.3;box-shadow:0 4px 10px rgba(0,0,0,.12)}
.services{position:absolute;left:34px;top:762px;list-style:none;font-size:17px;line-height:26px;color:var(--ink);border-left:2px dashed var(--pink);padding-left:18px}
.services li{position:relative}
.services li::before{content:"";position:absolute;left:-25px;top:7px;width:12px;height:12px;border-radius:50%;background:var(--gold)}
.pitch{position:absolute;left:475px;top:556px;width:295px;font-size:15.5px;line-height:1.3;color:var(--pink);text-align:justify}
.pitch p+p{margin-top:8px}
.feature{position:absolute;text-align:center;font-size:13px;line-height:1.15;color:var(--ink)}
.feature svg{display:block;margin:0 auto 4px}
.feature-left{left:470px;width:150px}
.feature-right{left:630px;width:160px}
.contact{position:absolute;left:30px;top:1022px;color:#fff}
.contact-call{font-family:'Cinzel',serif;font-size:22px;letter-spacing:1px}
.contact-call strong{font-weight:700}
.contact-email{font-size:16px;margin-top:6px}
.web{position:absolute;right:30px;bottom:16px;color:#fff;font-size:16px;letter-spacing:2px}
</style>
</head>
<body>
<main class="leaflet">
  <svg class="leaflet-shapes" viewBox="0 0 800 1130" width="800" height="1130">
    <defs>
      <linearGradient id="pinkTop" x1="0" y1="0" x2="1" y2="1">
        <stop offset="0" stop-color="#d92a86"/><stop offset="1" stop-color="#f06aae"/>
      </linearGradient>
      <linearGradient id="goldBand" x1="0" y1="0" x2="1" y2="0">
        <stop offset="0" stop-color="#b8862e"/><stop offset=".5" stop-color="#e2bc62"/><stop offset="1" stop-color="#c4943a"/>
      </linearGradient>
      <linearGradient id="roomTones" x1="0" y1="0" x2="1" y2="1">
        <stop offset="0" stop-color="#8f847c"/><stop offset=".5" stop-color="#c9bdb2"/><stop offset="1" stop-color="#e4ddd6"/>
      </linearGradient>
      <linearGradient id="fadedTones" x1="0" y1="0" x2="1" y2="0">
        <stop offset="0" stop-color="#ffffff"/><stop offset=".5" stop-color="#ececec"/><stop offset="1" stop-color="#d8d8d8"/>
      </linearGradient>
    </defs>
    <path d="M0 0H800V150C560 155 250 240 0 400Z" fill="url(#pinkTop)"/>
    <path d="M0 412C250 252 560 165 800 160" fill="none" stroke="url(#goldBand)" stroke-width="12"/>
    <path d="M160 392C330 265 560 178 800 172V440C620 470 420 470 250 450Z" fill="url(#roomTones)" role="img" aria-label="Photograph of an elegant living room with fireplace, chandelier and cream sofa"/>
    <path d="M250 450C420 470 620 470 800 440V478C620 510 420 512 260 488Z" fill="url(#pinkTop)"/>
    <path d="M262 494C420 518 620 516 800 484V500C620 535 420 538 272 512Z" fill="url(#goldBand)"/>
    <path d="M560 760H800V1056H444C470 950 500 820 560 760Z" fill="url(#fadedTones)" role="img" aria-label="Faded photograph of a relaxed client at home"/>
    <path d="M0 998H410L450 1052H800V1058H446L406 1004H0Z" fill="var(--pink)"/>
    <path d="M0 1008H404L444 1062H800V1130H0Z" fill="url(#goldBand)"/>
    <circle cx="170" cy="420" r="118" fill="url(#goldBand)"/>
    <circle cx="170" cy="420" r="107" fill="#fff" stroke="var(--pink)" stroke-width="2"/>
  </svg>

  <p class="tagline">We look after our clients’ homes and holiday lets across South Somerset</p>

  <div class="logo-disc"><span class="logo-name">Hollowmere<br>Farm</span></div>

  <h1 class="title"><span class="title-main">Hollowmere Farm</span><span class="title-sub">Home Management</span></h1>

  <p class="intro-pill">The team @ Hollowmere Farm can help with every aspect of managing and enhancing your home including:</p>

  <ul class="services">
    <li>Regular housekeeping and professional cleaning</li>
    <li>Exit cleans</li>
    <li>One-off seasonal /party / building work cleans</li>
    <li>Laundry and ironing</li>
    <li>Chic and contemporary flower arrangements</li>
    <li>Car valeting</li>
    <li>Pet food delivery</li>
    <li>Dry cleaning</li>
  </ul>

  <div class="pitch">
    <p>We take pride in providing high-end, consistent and reliable professional services bespoke to you.</p>
    <p>Coming home to a beautiful environment and being able to relax and enjoy your time is something we all deserve.</p>
  </div>

  <div class="feature feature-left" style="top:755px">
    <svg width="48" height="48" viewBox="0 0 60 60"><circle cx="30" cy="30" r="27" fill="#fff" stroke="var(--gold)" stroke-width="4"/><path d="M19 31l8 8 15-17" fill="none" stroke="var(--pink)" stroke-width="4" stroke-linecap="round" stroke-linejoin="round"/></svg>
    Satisfaction<br>guaranteed</div>
  <div class="feature feature-left" style="top:850px">
    <svg width="48" height="48" viewBox="0 0 60 60"><circle cx="30" cy="30" r="27" fill="#fff" stroke="var(--gold)" stroke-width="4"/><circle cx="30" cy="30" r="15" fill="none" stroke="var(--pink)" stroke-width="3"/><path d="M24 36l12-12" stroke="var(--pink)" stroke-width="3"/><circle cx="25" cy="25" r="2.5" fill="var(--pink)"/><circle cx="35" cy="35" r="2.5" fill="var(--pink)"/></svg>
    Competitive<br>rates</div>
  <div class="feature feature-left" style="top:945px">
    <svg width="48" height="48" viewBox="0 0 60 60"><circle cx="30" cy="30" r="27" fill="#fff" stroke="var(--gold)" stroke-width="4"/><rect x="18" y="24" width="24" height="17" rx="2" fill="none" stroke="var(--pink)" stroke-width="3"/><path d="M25 24v-4h10v4" fill="none" stroke="var(--pink)" stroke-width="3"/></svg>
    Member of the<br>Staffing Standards<br>Guild</div>

  <div class="feature feature-right" style="top:790px">
    <svg width="48" height="48" viewBox="0 0 60 60"><circle cx="30" cy="30" r="27" fill="#fff" stroke="var(--gold)" stroke-width="4"/><path d="M30 40C18 31 20 20 26 20c2 0 4 2 4 4 0-2 2-4 4-4 6 0 8 11-4 16z" fill="none" stroke="var(--pink)" stroke-width="3"/></svg>
    Professional staff you<br>can trust and rely on</div>
  <div class="feature feature-right" style="top:885px">
    <svg width="48" height="48" viewBox="0 0 60 60"><circle cx="30" cy="30" r="27" fill="#fff" stroke="var(--gold)" stroke-width="4"/><path d="M30 16l12 5v9c0 8-6 13-12 15-6-2-12-7-12-15v-9z" fill="none" stroke="var(--pink)" stroke-width="3"/><path d="M24 30l4 4 8-8" fill="none" stroke="var(--pink)" stroke-width="3"/></svg>
    CRB checked<br>and referenced</div>
  <div class="feature feature-right" style="top:975px">
    <svg width="48" height="48" viewBox="0 0 60 60"><circle cx="30" cy="30" r="27" fill="#fff" stroke="var(--gold)" stroke-width="4"/><path d="M30 16l12 5v9c0 8-6 13-12 15-6-2-12-7-12-15v-9z" fill="none" stroke="var(--pink)" stroke-width="3"/><path d="M30 24v12M24 30h12" stroke="var(--pink)" stroke-width="3"/></svg>
    Fully Insured</div>

  <div class="contact">
    <p class="contact-call">Call us today <strong>07700 900123</strong></p>
    <p class="contact-email">E: info@hollowmerefarm-example.co.uk</p>
  </div>
  <p class="web">visit us-www.hollowmerefarm-example.co.uk</p>
</main>
</body>
</html>
```